TV graphics and overlay for the Korvath Cup broadcast event

can anyone help me with creating a package of various TV graphics for our TV produced table tennis event, Korvath Cup. www.korvathcup-example.com

Leaving you with some mock ups we need to make. Mostly graphics and overlay:

Scoreboard design:
Point score (game)
Point score Team World vs Team Asia
Total points
Bracket
Tournament schedule “today's Matches”
Replay
Winning shot

State posters:
Player Bio:
Name
Age
Ranking
Country
Favorite serve

Player Lineup\Team Bio:
Player Lineup for all team players

Motion:
Wipe
In and out of replay
Opening and closing animation (intro cheating vignette)
Moving background
Used for splitting etc.

DIV:
Split:
50/50
30/70
Moving background

Supring
Generic Names super
Plays great with Team design
Place super
Supring to commentator

Need to get it in layers\layers so things can be animated again in the graphics machine.
If you can make it in photoshop and after effects, it's nice to get the projects as well, then we can possibly split up the teams themselves.

Moving backgrounds can be delivered as 1080p50 Apple Prores HQ.
Stills: 1920 x 1080 .png

It would be nice if an inspection of the graphics with animation is provided, so that those who will implement it in the graphics unwinding machine have a reference to follow.
Need to get it in layers\layers so things can be animated again in the graphics machine. Also we have a Font package and a description of which fonts are to be used.
If you make it in photoshop and after effects, it's nice to get the projects as well, then we can possibly split up the teams themselves.

Stills: 1920 x 1080 .png

Target Market(s)

Global TV market, emphasis in Asia

Industry/Entity Type

Sports, table tennis

Requirements
Nice to have
• Like the mock ups

```html
<!DOCTYPE html>
<html lang="en">
<head>
<meta charset="utf-8">
<title>Korvath Cup – Broadcast Graphics</title>
<link rel="stylesheet" href="https://fonts.googleapis.com/css2?family=Jost:wght@400;500&display=swap">
<style>
  :root {
    --bg: #6b6b6b;
    --red: #e81e10;
    --red-accent: #c0150c;
    --red-bright: #e40d07;
    --red-dark: #560805;
    --black: #050505;
    --charcoal: #2a2a2a;
    --frame: #333333;
    --white: #ffffff;
    --caption: #f0f0f0;
  }
  html, body {
    margin: 0;
    padding: 0;
    width: 1067px;
    height: 1200px;
    overflow: hidden;
    background: var(--bg);
  }
  .graphics-sheet {
    display: block;
    width: 1067px;
    height: 1200px;
    font-family: "Jost", sans-serif;
  }
  .label { fill: var(--white); font-size: 42px; font-weight: 400; }
  .score { fill: var(--black); font-size: 40px; font-weight: 400; }
  .score-red { fill: var(--red-accent); font-size: 40px; font-weight: 400; }
  .caption { fill: var(--caption); font-size: 30px; font-weight: 400; }
  .fill-red { fill: var(--red); }
  .fill-red-accent { fill: var(--red-accent); }
  .fill-red-bright { fill: var(--red-bright); }
  .fill-red-dark { fill: var(--red-dark); }
  .fill-white { fill: var(--white); }
  .fill-black { fill: var(--black); }
  .fill-charcoal { fill: var(--charcoal); }
  .fill-frame { fill: var(--frame); }
  .outline-white { fill: none; stroke: var(--white); stroke-width: 1.2; }
  .stop-black { stop-color: var(--black); }
  .stop-charcoal { stop-color: var(--charcoal); }
  .stop-red-dark { stop-color: var(--red-dark); }
  .stop-red { stop-color: var(--red); }
</style>
</head>
<body>
<svg class="graphics-sheet" viewBox="0 0 960 1080" xmlns="http://www.w3.org/2000/svg">
  <defs>
    <linearGradient id="grad-asia" x1="0" x2="1" y1="0" y2="0">
      <stop offset="0" class="stop-black"/>
      <stop offset="0.55" class="stop-charcoal"/>
      <stop offset="1" class="stop-charcoal"/>
    </linearGradient>
    <linearGradient id="grad-world" x1="0" x2="1" y1="0" y2="0">
      <stop offset="0" class="stop-red-dark"/>
      <stop offset="0.55" class="stop-red"/>
      <stop offset="1" class="stop-red"/>
    </linearGradient>
    <filter id="box-shadow" x="-10%" y="-20%" width="130%" height="160%">
      <feDropShadow dx="2" dy="3" stdDeviation="3" flood-opacity="0.45"/>
    </filter>
  </defs>

  <!-- Player score bug -->
  <g class="score-bug">
    <rect class="fill-red-accent" x="49" y="187" width="19" height="68"/>
    <rect class="fill-red-accent" x="73" y="187" width="462" height="68"/>
    <polygon class="fill-white" points="533,187 651,187 651,255 533,255 513,221"/>
    <text class="label" x="90" y="235">LENA OSK VARDEN</text>
    <circle class="fill-red-accent" cx="542" cy="221" r="4.5"/>
    <text class="score-red" x="573" y="235" text-anchor="middle">6</text>
    <text class="score-red" x="626" y="235" text-anchor="middle">4</text>
  </g>

  <!-- Team scoreboard -->
  <g class="team-score team-asia">
    <polygon class="fill-frame" points="41,353 550,353 570,395 550,437 41,437"/>
    <polygon fill="url(#grad-asia)" points="44,356 547,356 566,395 547,434 44,434"/>
    <polygon class="outline-white" points="46,360 544,360 562,395 544,430 46,430"/>
    <polygon class="fill-white" points="597,353 697,353 697,437 597,437 574,395"/>
    <text class="label" x="78" y="408">TEAM ASIA</text>
    <text class="score" x="640" y="409" text-anchor="middle">6</text>
  </g>
  <g class="team-score team-world">
    <polygon class="fill-red-dark" points="41,464 550,464 570,506 550,548 41,548"/>
    <polygon fill="url(#grad-world)" points="44,467 547,467 566,506 547,545 44,545"/>
    <polygon class="outline-white" points="46,471 544,471 562,506 544,541 46,541"/>
    <polygon class="fill-white" points="597,464 697,464 697,548 597,548 574,506"/>
    <text class="label" x="78" y="519">TEAM WORLD</text>
    <text class="score" x="640" y="520" text-anchor="middle">4</text>
  </g>

  <!-- Team name bars -->
  <g class="team-bar team-world">
    <polygon fill="url(#grad-world)" points="45,605 665,605 610,683 45,683"/>
    <polygon class="fill-red" points="688,605 713,605 657,683 632,683"/>
    <polygon class="fill-red" points="735,605 760,605 704,683 679,683"/>
    <polygon class="fill-red" points="781,605 806,605 750,683 725,683"/>
    <text class="label" x="78" y="658">TEAM WORLD</text>
  </g>
  <g class="team-bar team-asia">
    <polygon fill="url(#grad-asia)" points="45,718 665,718 610,795 45,795"/>
    <polygon class="fill-charcoal" points="688,718 713,718 657,795 632,795"/>
    <polygon class="fill-charcoal" points="735,718 760,718 704,795 679,795"/>
    <polygon class="fill-charcoal" points="781,718 806,718 750,795 725,795"/>
    <text class="label" x="78" y="771">TEAM ASIA</text>
  </g>

  <!-- Name super -->
  <g class="name-super">
    <rect class="fill-red-bright" x="49" y="922" width="19" height="103"/>
    <rect class="fill-black" x="74" y="922" width="412" height="70" filter="url(#box-shadow)"/>
    <text class="label" x="90" y="970">LENA OSK VARDEN</text>
    <text class="caption" x="92" y="1023">Captain, Team World</text>
  </g>
</svg>
</body>
</html>
```